New Writer Needs Website to Showcase Her Work

I'm a new writer of literary fiction. Several of my short stories have been published in literary journals, with more to come. I'm working on my first novel, and one of my stories will be featured in a "best of" anthology that will hit bookstores soon. I am not online at all at the moment (allergic to social media), but I would like readers, editors and agents to be able to find me if they like my work. Also, I'm told that editors and agents are more likely to take a chance with a writer who promotes her work online, hence my project. I've uploaded a few of my (very short) stories to give you the flavor of who I am as a writer. I write for adults, and my fiction has a dark edge to it. Not Harold Vance dark, not BRV dark, more like unhappy people trying to make their way in a world that demands happiness. If I were so lucky as to write a movie, I'd write a quirky, brooding, independent film, not a summer blockbuster. Think Lanterns Over Pellworth, not Avalanche. Thank you for your help!

Target Market(s)

Literary editors, agents, publishers and readers.

Industry/Entity Type

Work

Logo Text

Tessa Ward Finch

Number of Pages Required

1 page

Font styles to use
Serif
Sans Serif

Colors

Designer to choose colors to be used in the design.

Requirements
Must have
• Weight. I write serious stories, and I want that to come through. I will want to add links to my stories that are published online, notices for upcoming speaking engagements, publications, news, etc. I'll want a Bio section or page. I really don't know how many pages would be optimal, so I'm open to suggestions.
Nice to have
• Darker colors, but not anything obvious like black. Please resist the temptation to incorporate roses into your design.
Should not have
• Anything cute or fussy. I like clean lines, simple designs that draw you in with their beauty.

```html
<!DOCTYPE html>
<html lang="en">
<head>
<meta charset="utf-8">
<title>Single Chapters – Blog</title>
<link href="https://fonts.googleapis.com/css2?family=Karla:wght@400;700&family=Arimo:wght@700&display=swap" rel="stylesheet">
<style>
  :root{
    --stage:#d3d3d3;
    --page:#ffffff;
    --ink:#111111;
    --bar:#121212;
    --text:#1c1c1c;
    --muted:#555555;
    --rule:#222222;
    --on-dark:#ffffff;
  }
  *{box-sizing:border-box;margin:0;padding:0}
  html,body{width:1075px;height:1200px;overflow:hidden;background:var(--stage)}
  body{font-family:"Karla",Arial,sans-serif;color:var(--text);position:relative}
  .page{position:absolute;left:130px;top:104px;width:845px;height:1096px;background:var(--page);overflow:hidden}
  .topbar{position:absolute;left:0;top:0;width:845px;height:26px;background:var(--bar)}
  .topbar svg{position:absolute;top:6px}
  .logo{position:absolute;left:350px;top:0;width:148px;height:31px;background:var(--ink);color:var(--on-dark);
    font-family:"Arimo",Arial,sans-serif;font-weight:700;font-size:18px;display:flex;align-items:center;justify-content:center}

  .post-photo{position:absolute;left:42px;width:503px;height:291px}
  .photo-grass{top:39px;background:linear-gradient(160deg,#6d6157 0%,#8a7c70 35%,#5a5148 65%,#3f4034 100%)}
  .photo-window{top:590px;background:linear-gradient(180deg,#1c1a18 0%,#3e3a36 30%,#57534e 55%,#201e1c 80%,#121110 100%)}
  .post-meta{position:absolute;left:56px;width:475px;display:flex;justify-content:space-between;align-items:center;color:var(--on-dark);font-weight:700}
  .meta-1{top:57px;font-size:15px}
  .meta-2{top:608px;font-size:11.5px}
  .author{display:flex;align-items:center;gap:5px}
  .author-dot{width:20px;height:20px;border:2px solid #fff;border-radius:50%;background:#1a1a1a}
  .meta-right{display:flex;align-items:center;gap:9px;font-size:11.5px}
  .meta-right span{display:flex;align-items:center;gap:4px}

  .post-card{position:absolute;left:66px;width:455px;background:var(--page);text-align:center}
  .card-1{top:290px}
  .card-2{top:841px}
  .post-title{font-weight:700;font-size:23px;color:var(--ink);padding-top:20px;line-height:28px}
  .post-category{font-size:8.5px;text-transform:uppercase;letter-spacing:.3px;margin-top:7px}
  .post-excerpt{text-align:left;font-size:11.9px;line-height:23.3px;margin:11px 0 0 21px;width:420px}
  .post-excerpt .line{display:block;white-space:nowrap}
  .read-more{display:block;width:137px;height:23px;margin:17px auto 0;background:var(--ink);color:var(--on-dark);
    font-size:8.5px;font-weight:700;line-height:23px;text-transform:uppercase}

  .sidebar{position:absolute;left:571px;top:0;width:227px}
  .widget-title{position:absolute;left:0;width:227px;height:28px;border-left:1.5px solid var(--rule);border-bottom:1.5px solid var(--rule);
    font-size:8.5px;text-transform:uppercase;padding-left:7px;line-height:28px}
  .tile{position:absolute;left:0;width:227px;height:87px;color:var(--on-dark);font-weight:700}
  .tile-name{position:absolute;left:9px;bottom:10px;font-size:13px;line-height:17px}
  .tile-count{position:absolute;right:8px;top:6px;font-size:11px;display:flex;gap:3px;align-items:center}
  .t1{top:88px;background:linear-gradient(160deg,#a3968b,#6e645b 60%,#4b4740)}
  .t2{top:178px;background:linear-gradient(120deg,#4a3426,#6d4b35 50%,#2f2721)}
  .t3{top:268px;background:linear-gradient(180deg,#5a5a5a,#2a2a2a 60%,#141414)}
  .t4{top:357px;background:linear-gradient(150deg,#1f3a2e,#2f4f3c 50%,#14261d)}
  .t5{top:447px;background:linear-gradient(180deg,#3a3836,#56524e 50%,#1e1c1a)}
  .ad{position:absolute;left:0;top:546px;width:227px;height:226px;background:linear-gradient(160deg,#7a5a48,#b2664a 30%,#3d2418 60%,#24140c)}
  .ad::after{content:"";position:absolute;left:6px;top:6px;right:6px;bottom:6px;border:2px solid rgba(255,255,255,.85)}
  .ad-note{position:absolute;left:0;top:775px;font-size:10.5px;font-style:italic}
  .about{position:absolute;left:0;top:840px;width:227px;text-align:center}
  .avatar{width:98px;height:98px;border-radius:50%;border:3px solid #e6e6e6;background:radial-gradient(circle at 40% 40%,#3a3a3a,#0d0d0d);margin:3px auto 0}
  .about-name{font-family:"Arimo",Arial,sans-serif;font-weight:700;font-size:18px;margin-top:15px;color:var(--ink)}
  .about-bio{font-size:11.3px;line-height:16.3px;margin-top:5px}
  .about-icons{display:flex;justify-content:center;gap:12px;margin-top:11px}
</style>
</head>
<body>
<main class="page">
  <header class="topbar">
    <svg style="left:52px" width="15" height="15" viewBox="0 0 15 15"><circle cx="6" cy="6" r="4.3" fill="none" stroke="#fff" stroke-width="2"/><line x1="9.2" y1="9.2" x2="13.5" y2="13.5" stroke="#fff" stroke-width="2.4"/></svg>
    <svg style="left:783px" width="15" height="13" viewBox="0 0 15 13"><rect y="0" width="15" height="2.4" fill="#fff"/><rect y="5.3" width="15" height="2.4" fill="#fff"/><rect y="10.6" width="15" height="2.4" fill="#fff"/></svg>
    <div class="logo">Your Logo</div>
  </header>

  <article>
    <div class="post-photo photo-grass" role="img" aria-label="Soft-focus photo of pampas grass plumes"></div>
    <div class="post-meta meta-1">
      <span class="author"><span class="author-dot"></span>written by your name</span>
      <span class="meta-right">
        <span><svg width="11" height="11" viewBox="0 0 11 11"><rect x=".8" y="1.8" width="9.4" height="8.4" fill="none" stroke="#fff" stroke-width="1.3"/><line x1=".8" y1="4.3" x2="10.2" y2="4.3" stroke="#fff" stroke-width="1.3"/></svg>December 31, 2016</span>
        <span><svg width="12" height="11" viewBox="0 0 12 11"><path d="M6 1C3 1 1 2.8 1 5s2 4 5 4c.6 0 1.2-.1 1.7-.2L10.5 10 10 7.6C10.6 6.9 11 6 11 5c0-2.2-2-4-5-4z" fill="none" stroke="#fff" stroke-width="1.2"/></svg>12</span>
      </span>
    </div>
    <div class="post-card card-1">
      <h2 class="post-title">Your decisions</h2>
      <p class="post-category">Single Chapters</p>
      <p class="post-excerpt">
        <span class="line">The fascination of speculation was strong upon me. It was as though I had</span>
        <span class="line">been carried back to the birth time of our own outer world to look upon its</span>
        <span class="line">lands and seas ages before man had traversed either. Here was a new world,</span>
        <span class="line">all untouched. It called to me to explore it. I was dreaming of the excitement</span>
        <span class="line">and adventure which lay before us could Perry and I but escape the Mahars,</span>
        <span class="line">when something, a slight noise I imagine, drew my attention behind me.</span>
      </p>
      <span class="read-more">Read More</span>
    </div>
  </article>

  <article>
    <div class="post-photo photo-window" role="img" aria-label="Dark photo of potted succulents on a windowsill"></div>
    <div class="post-meta meta-2">
      <span class="author"><span class="author-dot"></span>written by Marcel</span>
      <span class="meta-right">
        <span><svg width="11" height="11" viewBox="0 0 11 11"><rect x=".8" y="1.8" width="9.4" height="8.4" fill="none" stroke="#fff" stroke-width="1.3"/><line x1=".8" y1="4.3" x2="10.2" y2="4.3" stroke="#fff" stroke-width="1.3"/></svg>December 20, 2016</span>
        <span><svg width="12" height="11" viewBox="0 0 12 11"><path d="M6 1C3 1 1 2.8 1 5s2 4 5 4c.6 0 1.2-.1 1.7-.2L10.5 10 10 7.6C10.6 6.9 11 6 11 5c0-2.2-2-4-5-4z" fill="none" stroke="#fff" stroke-width="1.2"/></svg>1</span>
      </span>
    </div>
    <div class="post-card card-2">
      <h2 class="post-title">Like Yesterday</h2>
      <p class="post-category">Single Chapters</p>
      <p class="post-excerpt">
        <span class="line">The three boys were now hard at it; and quite a knocking and hammering</span>
        <span class="line">arose, in which Granser babbled on unnoticed. "You are true savages. Already</span>
        <span class="line">has begun the custom of wearing human teeth. In another generation you will</span>
        <span class="line">be perforating your noses and ears and wearing ornaments of bone and shell.</span>
        <span class="line">I know.</span>
      </p>
    </div>
  </article>

  <aside class="sidebar">
    <h3 class="widget-title" style="top:44px">Most Commented</h3>
    <div class="tile t1" role="img" aria-label="Pampas grass thumbnail"><span class="tile-count">💬︎12</span><span class="tile-name">Your decisions</span></div>
    <div class="tile t2" role="img" aria-label="Autumn boardwalk thumbnail"><span class="tile-count">💬︎7</span><span class="tile-name">Alone</span></div>
    <div class="tile t3" role="img" aria-label="City street thumbnail"><span class="tile-count">💬︎4</span><span class="tile-name">The story behind our<br>city</span></div>
    <div class="tile t4" role="img" aria-label="Green leaves thumbnail"><span class="tile-count">💬︎2</span><span class="tile-name">Come Closer</span></div>
    <div class="tile t5" role="img" aria-label="Windowsill plants thumbnail"><span class="tile-count">💬︎1</span><span class="tile-name">Like Yesterday</span></div>
    <div class="ad" role="img" aria-label="Advertisement photo of a coffee tin on coffee beans"></div>
    <p class="ad-note">this is an advertisement</p>
    <h3 class="widget-title" style="top:798px">Behind Quillmark</h3>
    <section class="about">
      <div class="avatar" role="img" aria-label="Author portrait"></div>
      <p class="about-name">Your Name</p>
      <p class="about-bio">Hi! I am Marcel, the author of<br>Quillmark. This is a PressLeaf theme<br>created with a simple goal in mind:<br>to give you an opportunity to write<br>easily and easily be read.</p>
      <div class="about-icons">
        <svg width="11" height="9" viewBox="0 0 11 9"><rect x=".6" y=".6" width="9.8" height="7.8" fill="none" stroke="#777" stroke-width="1.2"/><path d="M.6 .8 5.5 5 10.4 .8" fill="none" stroke="#777" stroke-width="1.2"/></svg>
        <svg width="11" height="10" viewBox="0 0 11 10"><path d="M5.5 0 0 4.8h1.5V10h3V6.8h2V10h3V4.8H11z" fill="#777"/></svg>
      </div>
    </section>
  </aside>
</main>
</body>
</html>
```